" Nossa empresa já possui um público ativo, que necessita de nossos serviços, ou seja, não precisamos trabalhar com a capacitação de clientes. Atendemos na grande maioria advogados, oficiais de justiça, servidores públicos, e por isso queremos uma marca de confiança, sólida e com personalidade. "

```html
<!DOCTYPE html>
<html lang="pt-BR">
<head>
<meta charset="utf-8">
<title>Registro Serra Azul – Papelaria</title>
<link href="https://fonts.googleapis.com/css2?family=Montserrat:wght@400;500&display=swap" rel="stylesheet">
<style>
  :root {
    --brand: #a65a43;
    --paper: #ffffff;
    --paper-edge: #e4e4e4;
    --flap: #f3f3f3;
    --backdrop: #ececec;
    --text: #4a4a4a;
    --watermark: #f0f0f0;
  }
  * { margin: 0; padding: 0; box-sizing: border-box; }
  html, body { width: 1200px; height: 1200px; overflow: hidden; }
  body {
    background: var(--backdrop);
    font-family: "Montserrat", sans-serif;
    position: relative;
  }
  .letter-sheet {
    position: absolute;
    left: 91px; top: 341px;
    width: 486px; height: 640px;
    background: var(--paper);
    box-shadow: 0 2px 8px rgba(0,0,0,0.12);
  }
  .letter-watermark {
    position: absolute;
    left: 0; right: 0; top: 230px;
    text-align: center;
    font-size: 76px;
    font-weight: 400;
    color: var(--watermark);
    letter-spacing: 4px;
  }
  .letter-footer {
    position: absolute;
    left: 38px; right: 30px; top: 563px;
    display: flex;
    gap: 32px;
    font-size: 10.5px;
    line-height: 15px;
    color: var(--text);
  }
  .contact-list { list-style: none; }
  .contact-list li { display: flex; align-items: center; gap: 5px; }
  .contact-icon {
    width: 10px; height: 10px; border-radius: 50%;
    background: var(--brand);
    display: inline-flex; align-items: center; justify-content: center;
    flex: none;
  }
  .contact-icon svg { width: 6px; height: 6px; }
  .address { display: flex; gap: 5px; }
  .address .contact-icon { margin-top: 2px; }
  .letter-band {
    position: absolute;
    left: 0; bottom: 0;
    width: 100%; height: 10px;
  }
  .envelope {
    position: absolute;
    left: 580px; top: 185px;
    width: 500px; height: 830px;
  }
  .envelope-brand {
    position: absolute;
    left: 690px; top: 566px;
    width: 250px;
    display: flex; align-items: center; gap: 12px;
    color: var(--brand);
    font-weight: 500;
    font-size: 28px;
    line-height: 1.1;
    letter-spacing: 1px;
    text-transform: uppercase;
  }
  .brand-square {
    width: 22px; height: 22px;
    background: var(--brand);
    flex: none;
  }
</style>
</head>
<body>

<section class="letter-sheet">
  <div class="letter-watermark">Serra Azul</div>
  <footer class="letter-footer">
    <ul class="contact-list">
      <li><span class="contact-icon"><svg viewBox="0 0 6 6"><rect x="0.5" y="1.2" width="5" height="3.6" fill="none" stroke="#fff" stroke-width="0.8"/></svg></span>contato@serraazul.com.br</li>
      <li><span class="contact-icon"><svg viewBox="0 0 6 6"><path d="M1 1 L2.3 1 L2.8 2.3 L2 2.9 Q2.8 4 3.4 4 L4 3.2 L5 3.7 L5 5 Q2 5 1 1 Z" fill="#fff"/></svg></span>+55 (47) 3100-2200</li>
      <li><span class="contact-icon"><svg viewBox="0 0 6 6"><circle cx="3" cy="3" r="2.3" fill="none" stroke="#fff" stroke-width="0.7"/></svg></span>www.serraazul.com.br</li>
    </ul>
    <div class="address">
      <span class="contact-icon"><svg viewBox="0 0 6 6"><path d="M3 0.5 A1.8 1.8 0 0 1 4.8 2.3 Q4.8 3.6 3 5.5 Q1.2 3.6 1.2 2.3 A1.8 1.8 0 0 1 3 0.5 Z" fill="#fff"/></svg></span>
      <p>Rua das Acácias, nº 412, 2º Andar<br>Edifício Central Park, Bairro Jardim<br>CEP 89.100-000 - Serra Azul/SC</p>
    </div>
  </footer>
  <svg class="letter-band" viewBox="0 0 486 10" preserveAspectRatio="none"><path d="M0 2 H470 Q486 2 486 10 H0 Z" fill="var(--brand)"/></svg>
</section>

<svg class="envelope" viewBox="0 0 500 830">
  <polygon class="side-flap" points="462,85 490,105 490,815 462,825" fill="var(--flap)" stroke="var(--paper-edge)" stroke-width="1"/>
  <rect class="envelope-body" x="8" y="85" width="454" height="745" fill="var(--paper)" stroke="var(--paper-edge)" stroke-width="1"/>
  <path class="top-flap" d="M8 85 L8 20 Q8 8 20 8 H450 Q462 8 462 20 L462 85 Z" fill="var(--brand)"/>
  <path class="bottom-band" d="M8 795 H425 Q440 795 442 810 H8 Z" fill="var(--brand)"/>
</svg>

<div class="envelope-brand">
  <span class="brand-square"></span>
  <span>Registro<br>Serra Azul</span>
</div>

</body>
</html>
```